Brisk Bookings needs a New Home page

We provide online appointment scheduling. There are many schedulers out there. Ours is unique because the scheduler is shown in one compact view that can be easily incorporated into the customer's website or Chatterloop page. Whether our customer is a solo hair-stylist or a large testing center with hundreds of testing seats at multiple locations, our customer still gets the same easy-to-use, one-page scheduling experience.

Our current home page, briskbookings.com, feels cluttered and outdated. We want something more modern and minimal.

Here are web pages we like:
plumtrellis.com
fernquay.com
gossamo.io

We are not unhappy with the current logo or color scheme.

Need very clear call(s) to action (i.e. sign up for trial, schedule a demo).
Design needs to look good on devices of varying size.

Here are some ideas:
“Simple Online Scheduling” - Simple, compact design, easy-to-use & powerful, time-saving, chaos-taming, affordable, one page scheduling
“Stay in touch” - Basic email confirmations, reminders or targeted email notifications for follow-ups, no shows and more
“Multiple locations? No problem” - Schedule for multiple locations on one scheduler -
“Resource Pools” - Batting cages, clerks at the BQT, computers in a lab, pilates reformer machines
“Go Social” - Scheduling for Chatterloop and mobile devices
“Visual Reporting” - Reports
“Trusted” - Testimonials, reliable since 2005, etc.
List of industries (with links to industry-specific pages)

Ultimately want to redevelop the full site.

Reason: Please do not submit any new designs. We are now just wrapping up polling and discussing details. Thank you to all designers who have submitted. We feel lucky to get to chose from many great designs.

Target Market(s)

Audience is very broad including solo entrepreneurs (massage therapist, accountants, lawyers), educational institutions (elementary schools, university departments, advisers, testing centers), health care providers and screening services, to government.

Industry/Entity Type

Online

Requirements
Must have
• Call(s) to action, i.e. sign up for trial, schedule a demo.
• Look good on devices of different sizes.

```html
<!DOCTYPE html>
<html lang="en">
<head>
<meta charset="utf-8">
<title>Brisk Bookings – Simple Online Scheduling</title>
<link rel="stylesheet" href="https://fonts.googleapis.com/css2?family=Open+Sans:wght@300;400;600&display=swap">
<style>
:root{
  --blue:#1ba3dc;
  --blue-band:rgba(27,170,226,.92);
  --orange:#f7941d;
  --accent:#e8782a;
  --ink:#3a3a3a;
  --muted:#666;
  --rule:#d9d9d9;
  --dark:#363f47;
  --icon:#b8b8b8;
  --foot:#f8f8f8;
  --bar:#e9eaec;
}
*{margin:0;padding:0;box-sizing:border-box}
html,body{width:1200px;height:2278px;overflow:hidden}
body{font-family:"Open Sans",Arial,sans-serif;color:var(--ink);background:#fff;position:relative}
.abs{position:absolute}

.site-header{position:absolute;left:0;top:0;width:1200px;height:116px;background:#fff}
.brand{position:absolute;left:70px;top:48px;display:flex;align-items:center;gap:10px;font-size:32px;font-weight:400;color:var(--blue);letter-spacing:-.5px}
.brand-dot{width:14px;height:14px;border-radius:50%;background:var(--orange)}
.btn{position:absolute;top:62px;height:34px;width:89px;border-radius:3px;color:#fff;font-size:14px;font-weight:600;text-align:center;line-height:34px}
.btn-signin{left:933px;background:var(--blue)}
.btn-login{left:1034px;background:var(--orange)}

.main-nav{position:absolute;left:0;top:116px;width:1200px;height:54px;background:linear-gradient(#fdfdfd,#ececec);border-top:1px solid #d4d4d4;border-bottom:1px solid #d4d4d4}
.main-nav ul{list-style:none;display:flex;position:absolute;left:76px;top:0;height:52px}
.main-nav li{height:52px;line-height:52px;font-size:16px;color:#444;text-align:center;border-right:1px solid #cfcfcf}
.main-nav li:last-child{border-right:0}

.hero{position:absolute;left:0;top:170px;width:1200px;height:447px;background:linear-gradient(120deg,#8a6a4a 0%,#c9c3bb 30%,#f2f2f2 55%,#e6e6e8 80%,#6d5440 100%)}
.hero-band{position:absolute;left:0;top:216px;width:602px;height:141px}
.hero-title{position:absolute;left:64px;top:240px;color:#fff;font-size:34px;font-weight:600;letter-spacing:.3px}
.hero-sub{position:absolute;left:65px;top:283px;color:#fff;font-size:16px;line-height:24px;width:470px}
.dots{position:absolute;left:542px;top:419px;display:flex;gap:4px}
.dots span{width:15px;height:15px;border-radius:50%;background:#777}
.dots span:first-child{background:#111}

.intro{position:absolute;left:0;top:662px;width:1200px;text-align:center}
.intro h1{font-size:36px;font-weight:400;color:#333}
.intro p{width:920px;margin:10px auto 0;font-size:15px;line-height:24px;color:var(--muted);font-weight:300}

.card{position:absolute;top:800px;width:344px;height:280px;border:1px solid #dcdcdc;border-radius:3px;background:linear-gradient(#fff 65%,#f0f0f0);text-align:center}
.card svg{position:absolute;left:50%;transform:translateX(-50%);top:33px}
.card h3{position:absolute;top:132px;width:100%;font-size:28px;font-weight:400;color:var(--blue)}
.card p{position:absolute;top:184px;left:40px;right:40px;font-size:14px;line-height:24px;color:#555}
.card-affordable h3{top:140px}
.card-affordable p{top:192px}

.notify{position:absolute;left:0;top:1124px;width:1200px;height:478px;background:var(--dark)}
.tablet{position:absolute;left:94px;top:64px;width:442px;height:340px;border-radius:10px;background:linear-gradient(#fff,#ececec);border:1px solid #cfcfcf}
.tablet-screen{position:absolute;left:36px;top:32px;width:364px;height:274px;background:radial-gradient(circle at 45% 60%,#5fd0f2 0%,#1c8fc4 45%,#0b5e8e 100%)}
.tablet-cam{position:absolute;left:16px;top:166px;width:6px;height:6px;border-radius:50%;background:#333}
.notify h2{position:absolute;left:586px;top:62px;font-size:36px;font-weight:300;color:#fff}
.notify h4{position:absolute;left:588px;top:117px;font-size:16px;font-weight:400;color:#fff}
.notify .copy{position:absolute;left:588px;top:150px;width:530px;font-size:13px;line-height:23.5px;color:#d5d9dc}
.notify .copy p+p{margin-top:23px}

.feature{position:absolute;top:1664px;width:330px}
.feature h2{font-size:36px;font-weight:300;color:var(--accent)}
.feature h5{margin-top:4px;font-size:18px;font-weight:400;color:#555}
.feature p{margin-top:14px;font-size:13.5px;line-height:24px;color:#666}
.feature p+p{margin-top:9px}

.site-footer{position:absolute;left:0;top:1952px;width:1200px;height:270px;background:var(--foot);border-top:1px solid #e2e2e2}
.foot-col{position:absolute;top:40px}
.foot-col h6{font-size:22px;font-weight:400;color:#444}
.foot-col ul{list-style:none;margin-top:6px}
.foot-col li{font-size:14px;line-height:25px;color:#777}
.foot-rule{position:absolute;top:42px;width:1px;height:171px;background:var(--rule)}
.social{display:flex;gap:5px;margin-top:10px}
.social span{width:30px;height:30px;border-radius:50%;background:#aaa}
.legal-bar{position:absolute;left:0;top:2221px;width:1200px;height:57px;background:var(--bar);font-size:14px;color:#555;line-height:57px;padding-left:84px}
</style>
</head>
<body>

<header class="site-header">
  <div class="brand"><span class="brand-dot"></span>briskbookings</div>
  <a class="btn btn-signin">SIGN IN</a>
  <a class="btn btn-login">LOG IN</a>
</header>

<nav class="main-nav">
  <ul>
    <li style="width:91px">HOME</li>
    <li style="width:149px">SEE IT WORK</li>
    <li style="width:152px">WHO ITS FOR</li>
    <li style="width:182px">OUR SCHEDULER</li>
    <li style="width:134px">FREE TRAIL</li>
    <li style="width:124px">CONTACT</li>
    <li style="width:128px">ABOUT US</li>
  </ul>
</nav>

<section class="hero">
  <div class="abs" style="inset:0" role="img" aria-label="Photo of a tablet and phone on a wooden desk showing a monthly budget chart"></div>
  <svg class="hero-band" viewBox="0 0 602 141" aria-hidden="true"><polygon points="0,0 602,0 565,141 0,141" fill="var(--blue-band)"/></svg>
  <h2 class="hero-title">SIMPLE ONLINE SCHEDULING</h2>
  <p class="hero-sub">Simple, compact design, easy-to-use &amp; powerful, time-saving, chaos-taming, affordable, one page scheduling</p>
  <div class="dots"><span></span><span></span><span></span><span></span></div>
</section>

<section class="intro">
  <h1>Mauris vel lacus vitae felis vestibulum volutpat</h1>
  <p>Duis tincidunt lectus quis dui viverra vestibulum. Suspendisse vulputate aliquam dui. Nulla elementum dui ut augue. Aliquam vehicula mi at mauris. Maecenas placerat, nisl at consequat rhoncus, sem nunc gravida justo, quis eleifend arcu velit quis lacus.</p>
</section>

<article class="card" style="left:64px">
  <svg width="90" height="90" viewBox="0 0 90 90" aria-hidden="true">
    <circle cx="45" cy="45" r="38" fill="none" stroke="var(--icon)" stroke-width="10"/>
    <path d="M45 24 V46 H60" fill="none" stroke="var(--icon)" stroke-width="6"/>
    <polygon points="0,44 18,30 22,52" fill="var(--icon)"/>
  </svg>
  <h3>Save Time</h3>
  <p>Lorem ipsum dolor sit amet consectetuer adipiscing elit Nam cursus Morbi ut Nullam enim leo</p>
</article>

<article class="card" style="left:428px">
  <svg width="90" height="90" viewBox="0 0 90 90" aria-hidden="true">
    <polygon points="4,14 14,4 36,26 40,14 40,40 14,40 26,36" fill="var(--icon)"/>
    <polygon points="86,76 76,86 54,64 50,76 50,50 76,50 64,54" fill="var(--icon)"/>
  </svg>
  <h3>Simplify</h3>
  <p>Lorem ipsum dolor sit amet consectetuer adipiscing elit Nam cursus Morbi ut Nullam enim leo</p>
</article>

<article class="card card-affordable" style="left:793px">
  <svg width="112" height="102" viewBox="0 0 112 102" aria-hidden="true">
    <rect x="3" y="3" width="106" height="66" fill="none" stroke="var(--icon)" stroke-width="6"/>
    <polyline points="16,52 30,36 40,46 54,28" fill="none" stroke="var(--icon)" stroke-width="4"/>
    <circle cx="82" cy="30" r="6" fill="var(--icon)"/>
    <rect x="72" y="42" width="20" height="12" fill="var(--icon)"/>
    <path d="M56 69 V82 M56 82 L30 100 M56 82 L82 100" stroke="var(--icon)" stroke-width="5"/>
  </svg>
  <h3>It’s Affordable</h3>
  <p>Lorem ipsum dolor sit amet consectetuer adipiscing elit Nam cursus Morbi ut Nullam enim leo</p>
</article>

<section class="notify">
  <div class="tablet">
    <span class="tablet-cam"></span>
    <div class="tablet-screen" role="img" aria-label="Illustration of a hand holding a phone with email envelopes flying out"></div>
  </div>
  <h2>Targeted Email Notifications</h2>
  <h4>Get the right information to the right person at the right time!</h4>
  <div class="copy">
    <p>Do you want to stay in touch with your clients? Want to set expectations and keep clients informed before an appointment? Would you like to follow up with a thank you or survey afterward? Or remind them to schedule their next appointment at the right time? Do you want to check in with clients who didn’t show up?</p>
    <p>Yes? Then, our targeted email notifications are for you! You control the timing and content of the email. Yet the system sends them out automatically. Just create a template, optionally tied to specific service, timed to go out when it makes the most sense relative to the appointment.</p>
  </div>
</section>

<section class="feature" style="left:76px">
  <h2>Affordable</h2>
  <h5>Phasellus felis dolor scelerisque</h5>
  <p>Vivamus porttitor, g, purus nisi eleifend libero, a tempus libero lectus feugiat felis. Morbi diam mauris, viverra in, gravida eu, mattis in, ante.</p>
  <p>Morbi porta, libero id ullamcorper mollis aliquam. Curabitur iaculis tempus eros.</p>
</section>
<section class="feature" style="left:445px">
  <h2>Easy to Use</h2>
  <h5>Phasellus felis dolor scelerisque</h5>
  <p>Vivamus porttitor, g, purus nisi eleifend libero, a tempus libero lectus feugiat felis. Morbi diam mauris, viverra in, gravida eu, mattis in, ante.</p>
  <p>Morbi porta, libero id ullamcorper mollis aliquam. Curabitur iaculis tempus eros.</p>
</section>
<section class="feature" style="left:817px">
  <h2>Powerfull</h2>
  <h5>Phasellus felis dolor scelerisque</h5>
  <p>Vivamus porttitor, g, purus nisi eleifend libero, a tempus libero lectus feugiat felis. Morbi diam mauris, viverra in, gravida eu, mattis in, ante.</p>
  <p>Morbi porta, libero id ullamcorper mollis aliquam. Curabitur iaculis tempus eros.</p>
</section>

<footer class="site-footer">
  <div class="foot-col" style="left:87px"><h6>Company</h6><ul><li>Cum sociis</li><li>Natoque penatibus</li><li>Magnis dis parturient</li><li>Montes nascetur</li><li>Ridiculus mus</li></ul></div>
  <span class="foot-rule" style="left:243px"></span>
  <div class="foot-col" style="left:283px"><h6>Company</h6><ul><li>Services Provide</li><li>Natoque penatibus</li><li>Montes nascetur</li><li>Ridiculus mus</li></ul></div>
  <span class="foot-rule" style="left:448px"></span>
  <div class="foot-col" style="left:480px"><h6>Support</h6><ul><li>Customer Service</li><li>Legal</li><li>Sitemap</li><li>Resources</li></ul></div>
  <span class="foot-rule" style="left:615px"></span>
  <div class="foot-col" style="left:655px"><h6>Sublinks</h6><ul><li>Services Provide</li><li>Natoque penatibus</li><li>Montes nascetur</li><li>Ridiculus mus</li></ul></div>
  <span class="foot-rule" style="left:814px"></span>
  <div class="foot-col" style="left:857px"><h6>Get Connected</h6><div class="social"><span></span><span></span><span></span><span></span></div></div>
</footer>

<div class="legal-bar">© 2013 Company Name.&nbsp; All right reserved.&nbsp; Term of Use</div>

</body>
</html>
```